Velvet Orchard - R&B Band in Sydney Requires new Business Cards

We're a 6 piece R&B Soul band in Sydney called Velvet Orchard that requires new promotional material including Business Cards.

We are very well known around Sydney and have a resident venue gig at the Marlowe Sydney hotel. We play predominantly old & new school R&B hits.

Our logo is attached, colours are Brown & yellow.
Initial idea was to get sugar packets made up with our logo and contact details.

```html
<!DOCTYPE html>
<html lang="en">
<head>
<meta charset="utf-8">
<title>Velvet Orchard – Sugar Packet Business Cards</title>
<link rel="stylesheet" href="https://fonts.googleapis.com/css2?family=Source+Sans+3:wght@400;700&display=swap">
<style>
  :root {
    --page-bg: #ffffff;
    --packet-light: #ecdcb8;
    --packet-mid: #dcc79a;
    --packet-dark: #c4ab78;
    --tab-brown: #6b5234;
    --logo-brown: #3a2415;
    --accent-red: #d8262e;
    --text-brown: #4d3a26;
    --text-body: #5b4732;
  }
  html, body {
    margin: 0;
    padding: 0;
    overflow: hidden;
    background: var(--page-bg);
  }
  .canvas {
    position: relative;
    width: 1050px;
    height: 1200px;
    overflow: hidden;
    background: var(--page-bg);
    font-family: "Source Sans 3", "Myriad Pro", sans-serif;
  }
  .packet {
    position: absolute;
    left: 187px;
    width: 675px;
    height: 582px;
    border-radius: 6px;
  }
  .packet--front { top: 5px; }
  .packet--back { top: 600px; width: 678px; height: 586px; }
  .packet__paper {
    position: absolute;
    inset: 0;
    border-radius: 6px;
    background:
      linear-gradient(180deg, var(--packet-mid) 0%, var(--packet-light) 12%, var(--packet-mid) 45%, var(--packet-light) 70%, var(--packet-dark) 92%, var(--packet-mid) 100%);
  }
  .packet__tab {
    position: absolute;
    top: 0;
    right: 42px;
    width: 32px;
    height: 58px;
    background: var(--tab-brown);
    border-radius: 3px;
  }
  .wordmark {
    position: absolute;
    margin: 0;
    color: var(--logo-brown);
    font-weight: 700;
    text-transform: uppercase;
    line-height: 0.92;
    letter-spacing: 0.02em;
    text-align: center;
  }
  .wordmark--large {
    left: 150px;
    top: 160px;
    width: 420px;
    font-size: 98px;
  }
  .wordmark--small {
    left: 385px;
    top: 100px;
    width: 185px;
    font-size: 44px;
  }
  .site-line {
    position: absolute;
    margin: 0;
    color: var(--logo-brown);
    font-weight: 400;
    text-align: center;
    opacity: 0.8;
  }
  .site-line--large {
    left: 140px;
    top: 398px;
    width: 440px;
    font-size: 21px;
    letter-spacing: 0.12em;
  }
  .site-line--small {
    left: 380px;
    top: 204px;
    width: 195px;
    font-size: 10px;
    letter-spacing: 0.08em;
  }
  .contact {
    position: absolute;
    left: 174px;
    top: 250px;
    margin: 0;
    font-style: normal;
  }
  .contact__name {
    margin: 0;
    color: var(--accent-red);
    font-size: 27px;
    font-weight: 400;
    line-height: 1;
  }
  .contact__role {
    margin: 6px 0 0 24px;
    color: var(--text-brown);
    font-size: 24px;
    line-height: 1;
  }
  .contact__line {
    margin: 0;
    color: var(--text-body);
    font-size: 20px;
    line-height: 1.35;
  }
  .contact__line--email { margin-top: 34px; }
  .contact__line--phone { margin-top: 20px; }
  .contact__line--web { margin-top: 28px; }
</style>
</head>
<body>
<main class="canvas">
  <section class="packet packet--front" aria-label="Business card front">
    <div class="packet__paper" role="img" aria-label="Crinkled sugar packet paper texture in sandy beige tones"></div>
    <div class="packet__tab"></div>
    <h1 class="wordmark wordmark--large">Velvet<br>Orchard</h1>
    <p class="site-line site-line--large">velvetorchardmusic.com.au</p>
  </section>

  <section class="packet packet--back" aria-label="Business card back">
    <div class="packet__paper" role="img" aria-label="Crinkled sugar packet paper texture in sandy beige tones"></div>
    <div class="packet__tab"></div>
    <h2 class="wordmark wordmark--small">Velvet<br>Orchard</h2>
    <p class="site-line site-line--small">velvetorchardmusic.com.au</p>
    <address class="contact">
      <p class="contact__name">LOREM IPSUM</p>
      <p class="contact__role">Voluptatem</p>
      <p class="contact__line contact__line--email">loremipsum@velvetorchard.com</p>
      <p class="contact__line contact__line--phone">607.555.0142</p>
      <p class="contact__line contact__line--web">http://www.velvetorchard.com</p>
      <p class="contact__line">Social: @velvetorchard</p>
    </address>
  </section>
</main>
</body>
</html>
```